HarmoNest Ensemble Jubilee
Date: Sunday Oct 2, 2022
When: 2-4 p.m.
Location: Brindle9 Alehouse
413 Marlowe Ct #200, Sacramento, CA 95821
Tickets: www.Tixolvo.com
General seating: $15 for adults and $10 for students

```html
<!DOCTYPE html>
<html lang="en">
<head>
<meta charset="utf-8">
<title>HarmoNest Ensemble Jubilee</title>
<link rel="stylesheet" href="https://fonts.googleapis.com/css2?family=Cinzel:wght@600;700&family=Cormorant+Garamond:wght@500;600;700&family=Italianno&display=swap">
<style>
  :root {
    --backdrop: #d9d9d9;
    --wine-deep: #1f0204;
    --wine: #5a0a0e;
    --crimson: #c8161c;
    --gold-light: #fff3c4;
    --gold: #e0b453;
    --gold-dark: #8a5a17;
    --cream: #f6ecd8;
    --white: #ffffff;
    --ink: #111111;
  }
  * { margin: 0; padding: 0; box-sizing: border-box; }
  html, body {
    width: 1039px;
    height: 1200px;
    overflow: hidden;
    background: var(--backdrop);
  }
  .poster {
    position: absolute;
    left: 54px;
    top: 0;
    width: 930px;
    height: 1200px;
    overflow: hidden;
    background:
      radial-gradient(ellipse 55% 40% at 40% 50%, rgba(200,22,28,0.85), rgba(200,22,28,0) 70%),
      radial-gradient(ellipse 40% 30% at 60% 58%, rgba(90,70,130,0.45), rgba(90,70,130,0) 70%),
      linear-gradient(180deg, var(--wine-deep) 0%, var(--wine) 45%, #3a0508 75%, var(--wine-deep) 100%);
    text-align: center;
    color: var(--cream);
  }
  .brand {
    position: absolute;
    top: 38px;
    left: 0;
    right: 0;
    font-family: "Cormorant Garamond", serif;
    font-weight: 600;
    font-size: 76px;
    line-height: 1;
    color: var(--white);
  }
  .subtitle {
    position: absolute;
    top: 150px;
    left: 0;
    right: 0;
    font-family: "Italianno", cursive;
    font-size: 78px;
    line-height: 1;
    color: var(--gold);
  }
  .headline {
    position: absolute;
    top: 215px;
    left: 0;
    right: 0;
    font-family: "Cinzel", serif;
    font-weight: 700;
    font-size: 118px;
    line-height: 1.1;
    letter-spacing: 2px;
    background: linear-gradient(180deg, var(--gold-light) 0%, var(--gold) 45%, var(--gold-dark) 100%);
    -webkit-background-clip: text;
    background-clip: text;
    color: transparent;
  }
  .date {
    position: absolute;
    top: 392px;
    left: 0;
    right: 0;
    font-family: "Cormorant Garamond", serif;
    font-weight: 500;
    font-size: 46px;
    color: var(--cream);
  }
  .rule {
    position: absolute;
    left: 200px;
    width: 530px;
    height: 2px;
    background: linear-gradient(90deg, rgba(224,180,83,0), var(--gold) 50%, rgba(224,180,83,0));
  }
  .rule--top { top: 458px; }
  .rule--bottom { top: 524px; }
  .time {
    position: absolute;
    top: 466px;
    left: 0;
    right: 0;
    font-family: "Cormorant Garamond", serif;
    font-weight: 700;
    font-size: 38px;
    color: var(--white);
  }
  .music-art {
    position: absolute;
    top: 530px;
    left: 0;
    width: 930px;
    height: 260px;
  }
  .foliage-art {
    position: absolute;
    bottom: 0;
    left: 0;
    width: 930px;
    height: 300px;
  }
  .venue {
    position: absolute;
    top: 842px;
    left: 0;
    right: 0;
    font-family: "Cormorant Garamond", serif;
    font-weight: 700;
    font-size: 42px;
    letter-spacing: 1px;
    color: var(--white);
  }
  .address {
    position: absolute;
    top: 910px;
    left: 0;
    right: 0;
    font-family: "Cormorant Garamond", serif;
    font-weight: 500;
    font-size: 35px;
    color: var(--white);
  }
  .tickets {
    position: absolute;
    top: 1024px;
    left: 217px;
    width: 490px;
    height: 44px;
    border-radius: 22px;
    background: linear-gradient(90deg, var(--gold) 0%, var(--gold-light) 50%, var(--gold) 100%);
    font-family: Arial, Helvetica, sans-serif;
    font-weight: 700;
    font-size: 23px;
    line-height: 44px;
    color: var(--ink);
  }
  .pricing {
    position: absolute;
    top: 1118px;
    left: 0;
    right: 0;
    font-family: Arial, Helvetica, sans-serif;
    font-weight: 700;
    font-size: 21px;
    letter-spacing: 0.3px;
    color: var(--white);
  }
</style>
</head>
<body>
  <main class="poster">
    <svg class="foliage-art" role="img" aria-label="Dark autumn leaves filling the lower part of the poster" viewBox="0 0 930 300" preserveAspectRatio="none">
      <defs>
        <linearGradient id="foliageFill" x1="0" y1="0" x2="0" y2="1">
          <stop offset="0" stop-color="#4a0a10" stop-opacity="0"/>
          <stop offset="0.5" stop-color="#3b0c12" stop-opacity="0.8"/>
          <stop offset="1" stop-color="#1d1a12"/>
        </linearGradient>
      </defs>
      <rect width="930" height="300" fill="url(#foliageFill)"/>
    </svg>

    <div class="brand">HarmoNest</div>
    <div class="subtitle">Barbershop Ensemble</div>
    <h1 class="headline">JUBILEE</h1>

    <p class="date">Sunday Oct 2, 2022</p>
    <div class="rule rule--top"></div>
    <p class="time">AT 2-4 P.M.</p>
    <div class="rule rule--bottom"></div>

    <svg class="music-art" role="img" aria-label="Glowing golden music staff with notes sweeping across the poster" viewBox="0 0 930 260" preserveAspectRatio="none">
      <defs>
        <radialGradient id="musicGlow" cx="0.5" cy="0.5" r="0.5">
          <stop offset="0" stop-color="#f2c66a" stop-opacity="0.35"/>
          <stop offset="1" stop-color="#f2c66a" stop-opacity="0"/>
        </radialGradient>
      </defs>
      <ellipse cx="465" cy="130" rx="465" ry="110" fill="url(#musicGlow)"/>
    </svg>

    <p class="venue">BRINDLE9 ALEHOUSE</p>
    <p class="address">413 Marlowe Ct #200, Sacramento, CA 95821</p>

    <div class="tickets">Tickets: www.Tixolvo.com</div>
    <p class="pricing">GENERAL SEATING: $15 FOR ADULTS &nbsp;•&nbsp; $10 FOR STUDENTS</p>
  </main>
</body>
</html>
```